Birchwell Chiropractic, achieve your health goals, get better each day one step at a time

A mobile friendly site, fresh look, easy to navigate, has interface with zq/chirplane, etc. Blog posts. Uses new logo. Content and address to current site is marvintoque.com. The current site will give you scope of project for content. The logo is not the final but close. Will upload final next week.
Convey the concept that heath is a process, it does not just happen. We take steps to achieve what we want in life including health.

Target Market(s)

30 to 70 year old. Needing health care

Industry/Entity Type

Health Care

Coding

Coded - Design and coding required

Number of Pages Required

5+ page

Font styles to use
Sans Serif

Colors

Designer to choose colors to be used in the design.

Requirements
Must have
• mobile friendly, easy to navigate, ZQ/Chirplane interface, blog, room for current content
Nice to have
• potential for commerce, statistics
Should not have
• Same old look and feel as everything else out there

```html
<!DOCTYPE html>
<html lang="en">
<head>
<meta charset="utf-8">
<title>Birchwell Chiropractic</title>
<link rel="stylesheet" href="https://fonts.googleapis.com/css2?family=Josefin+Sans:wght@400;600;700&family=EB+Garamond:wght@400;600;700&display=swap">
<style>
  :root {
    --navy: #1d3a55;
    --ink: #3c4650;
    --brand: #1f5a86;
    --topline: #3a6f96;
    --header-bg: #dedfe0;
    --divider: #a9bdcc;
    --white: #ffffff;
    --mist: #dde7ed;
    --footer: #415e76;
    --rule: #4a5561;
  }
  * { margin: 0; padding: 0; box-sizing: border-box; }
  html, body { width: 1200px; height: 2397px; overflow: hidden; background: var(--white); }
  .page { position: relative; width: 1200px; height: 2397px; overflow: hidden; font-family: "Josefin Sans", sans-serif; color: var(--navy); }
  .abs { position: absolute; }
  .h { line-height: 1; text-transform: uppercase; font-weight: 400; }
  .body-copy { font-family: "EB Garamond", serif; color: var(--ink); }

  .topline { left: 0; top: 0; width: 1200px; height: 8px; background: var(--topline); }
  .site-header { left: 0; top: 8px; width: 1200px; height: 101px; background: linear-gradient(#e6e7e8, #d6d8d9); box-shadow: 0 2px 4px rgba(0,0,0,.12); z-index: 2; }
  .brand { left: 93px; top: 36px; display: flex; align-items: center; gap: 12px; }
  .brand-dot { width: 26px; height: 26px; border-radius: 50%; background: var(--brand); }
  .brand-name { font-size: 27px; font-weight: 700; color: var(--brand); letter-spacing: 1px; text-transform: uppercase; line-height: 1; }
  .main-nav a { position: absolute; top: 58px; font-size: 17px; color: #2a3440; text-decoration: none; letter-spacing: .5px; line-height: 1; }

  .hero-photo { left: 0; top: 109px; width: 1200px; height: 594px;
    background: radial-gradient(ellipse at 35% 40%, #e9cdbd 0%, #d9b8a6 22%, transparent 48%),
                radial-gradient(ellipse at 85% 30%, #e6c7b5 0%, transparent 40%),
                linear-gradient(180deg, #d3d7da 0%, #eceeef 55%, #f6f7f8 100%); }
  .hero-title { left: 484px; top: 468px; font-size: 53px; letter-spacing: 1px; color: var(--navy); line-height: 1; }
  .hero-sub { left: 489px; font-size: 22px; letter-spacing: 1.5px; color: #2e3b48; }
  .hero-divider { left: 0; top: 703px; width: 1200px; height: 10px; background: var(--divider); }

  .intro-title { left: 93px; top: 756px; font-size: 44px; }
  .intro-sub { left: 95px; top: 815px; font-size: 22px; color: #3a4652; letter-spacing: .5px; }
  .emblem-art { left: 93px; top: 887px; width: 250px; height: 303px; background: radial-gradient(ellipse at 50% 50%, #7cc55a 0%, #b8e09f 45%, #ffffff 75%); }
  .link-heading { left: 431px; top: 772px; font-size: 22px; letter-spacing: .5px; }
  .link-rule { left: 411px; top: 810px; width: 351px; height: 2px; background: var(--rule); }
  .card-title { font-size: 22px; letter-spacing: .5px; }
  .card-text { font-size: 17.5px; line-height: 28px; }
  .read-more { font-size: 16px; letter-spacing: 1px; color: #3a4652; line-height: 1; }
  .hands-photo { left: 805px; top: 785px; width: 330px; height: 227px; background: linear-gradient(135deg, #f2f1f1 0%, #e6c9b9 45%, #d7ae98 70%, #eeeeee 100%); }

  .band { left: 0; top: 1251px; width: 1200px; height: 838px; background: var(--mist); }
  .welcome-title { left: 252px; width: 654px; top: 1307px; font-size: 33px; text-align: center; letter-spacing: 1px; }
  .welcome-rule { left: 252px; top: 1352px; width: 654px; height: 2px; background: var(--rule); }
  .welcome-text { left: 252px; top: 1371px; width: 700px; font-size: 18.5px; line-height: 27px; }
  .feature-title { left: 91px; top: 1604px; font-size: 37px; letter-spacing: 1px; }
  .band-text { font-size: 16.8px; line-height: 24.8px; }
  .small-heading { font-size: 17px; letter-spacing: .5px; font-weight: 600; }
  .knee-photo { left: 626px; top: 1801px; width: 509px; height: 235px; background: linear-gradient(120deg, #3b4a36 0%, #7a6f6a 30%, #c7a995 55%, #2d2f36 80%, #8a4c7a 100%); }

  .site-footer { left: 0; top: 2089px; width: 1200px; height: 308px; background: var(--footer); color: var(--white); }
  .foot-heading { top: 2180px; font-size: 17px; font-weight: 700; letter-spacing: 1px; line-height: 1; }
  .foot-serif { font-family: "EB Garamond", serif; font-weight: 700; font-size: 15px; color: var(--white); }
  .foot-small { font-size: 12px; font-weight: 700; letter-spacing: .5px; line-height: 1; }
  .foot-links { list-style: none; font-family: "EB Garamond", serif; font-weight: 700; font-size: 15px; line-height: 22.4px; text-transform: uppercase; }
</style>
</head>
<body>
<div class="page">
  <div class="abs topline"></div>
  <header class="abs site-header">
    <div class="abs brand" style="top:28px;">
      <span class="brand-dot"></span>
      <span class="brand-name">Birchwell Chiropractic</span>
    </div>
    <nav class="main-nav">
      <a style="left:590px;">HOME</a>
      <a style="left:671px;">SERVICES</a>
      <a style="left:780px;">PORTFOLIO</a>
      <a style="left:906px;">ABOUT</a>
      <a style="left:992px;">CONTACT</a>
    </nav>
  </header>

  <section>
    <div class="abs hero-photo" role="img" aria-label="Photo of a woman lying relaxed while a chiropractor supports her neck"></div>
    <h1 class="abs hero-title" style="font-weight:400;">Achieve your health goals</h1>
    <p class="abs h hero-sub" style="top:530px;">Get beter each day</p>
    <p class="abs h hero-sub" style="top:557px;">One step at a time</p>
    <div class="abs hero-divider"></div>
  </section>

  <section>
    <h2 class="abs h intro-title">Et quicit</h2>
    <p class="abs h intro-sub">Per quod multi serat</p>
    <div class="abs emblem-art" role="img" aria-label="Green illustration of a figure stretching in motion"></div>

    <h3 class="abs h link-heading">Per existent est quod &gt;</h3>
    <div class="abs link-rule"></div>

    <h3 class="abs h card-title" style="left:446px; top:857px;">Et ipsum quodque</h3>
    <p class="abs body-copy card-text" style="left:444px; top:903px; width:340px;">Sed in dui in augue consectetur lobortis. Pellentesque orci tellus, imperdiet interdum nibh a, varius gravida augue.</p>

    <h3 class="abs h card-title" style="left:446px; top:1036px;">Quomodo super</h3>
    <p class="abs body-copy card-text" style="left:444px; top:1081px; width:340px;">Sed in dui in augue consectetur lobortis. Pellentesque orci tellus, imperdiet interdum nibh a, varius gravida augue.</p>
    <span class="abs h read-more" style="left:623px; top:1204px;">Read more</span>

    <div class="abs hands-photo" role="img" aria-label="Photo of a therapist's hands treating a patient's hand"></div>
    <h3 class="abs h card-title" style="left:805px; top:1048px;">Et qui scit</h3>
    <p class="abs body-copy card-text" style="left:805px; top:1089px; width:330px;">Lorem ipsum dolor sit amet, consectetur adipiscing elit. Praesent hendrerit quis enim ac vehicula. Sed in dui in augue consectetur lobortis.</p>
  </section>

  <section>
    <div class="abs band"></div>
    <h2 class="abs h welcome-title">Welcome to our site</h2>
    <div class="abs welcome-rule"></div>
    <p class="abs body-copy welcome-text">Donec pretium mattis augue vel bibendum. Mauris non nibh in tortor placerat pharetra. Nunc ut lacinia elit. Mauris nec ante ac quam dictum suscipit. Sed orci quam, fringilla vitae semper at, venenatis vel tellus. Suspendisse lacinia laoreet turpis et blandit. Pellentesque habitant morbi tristique senectus et netus et malesuada fames ac turpis egestas.</p>

    <h2 class="abs h feature-title">Etiam at quoque</h2>
    <p class="abs body-copy band-text" style="left:91px; top:1663px; width:500px;">Quisque tincidunt quam a porta sagittis. Etiam at urna dolor. Curabitur semper, arcu ut consequat sagittis, arcu purus venenatis est, et tristique nibh nibh porttitor odio. Nunc blandit ac ante in accumsan. Vestibulum ac tincidunt eros. Suspendisse elementum in nisi ut fringilla. Suspendisse tincidunt orci sit amet tellus porta</p>

    <h3 class="abs h card-title" style="left:91px; top:1819px;">Et quique potest</h3>
    <p class="abs body-copy band-text" style="left:91px; top:1869px; width:500px;">Quisque tincidunt quam a porta sagittis. Etiam at urna dolor. Curabitur semper, arcu ut consequat sagittis, arcu purus venenatis est, et tristique nibh nibh porttitor odio. Nunc blandit ac ante in</p>

    <h3 class="abs h card-title" style="left:628px; top:1614px;">Perpit perlexa</h3>
    <p class="abs body-copy band-text" style="left:628px; top:1649px; width:510px;">Quisque tincidunt quam a porta sagittis. Etiam at urna dolor. Curabitur semper, arcu ut consequat sagittis, arcu purus venenatis est, et tristique nibh nibh porttitor odio. Nunc blandit ac ante in</p>
    <h4 class="abs h small-heading" style="left:628px; top:1748px;">Eternitatem magistima chose</h4>
    <div class="abs knee-photo" role="img" aria-label="Photo of a man seated outdoors holding his bandaged knee"></div>
  </section>

  <footer class="abs site-footer"></footer>
  <h4 class="abs h foot-heading" style="left:89px; color:var(--white);">Our location</h4>
  <p class="abs foot-serif" style="left:89px; top:2237px;">Lipsum quoque 10, et per</p>
  <p class="abs foot-serif" style="left:89px; top:2271px;">23, perque, Et sit</p>
  <span class="abs h foot-small" style="left:91px; top:2329px; color:var(--white);">See on maps</span>

  <h4 class="abs h foot-heading" style="left:454px; color:var(--white);">Links</h4>
  <ul class="abs foot-links" style="left:451px; top:2223px;">
    <li>Home</li><li>Portfolio</li><li>Services</li><li>About</li><li>Contact</li>
  </ul>

  <h4 class="abs h foot-heading" style="left:631px; color:var(--white);">About us</h4>
  <p class="abs foot-serif" style="left:631px; top:2235px; width:230px; line-height:22.4px;">Suspendisse aliquet purus et lectus consequat, vel auctor ante auctor. Nam et sapien</p>
  <span class="abs h foot-small" style="left:633px; top:2327px; color:var(--white);">Read more</span>

  <h4 class="abs h foot-heading" style="left:989px; color:var(--white);">Company</h4>
  <ul class="abs foot-links" style="left:986px; top:2223px;">
    <li>Pharetra</li><li>Ecit</li><li>Perque</li><li>Ed sae</li><li>Quoque</li>
  </ul>
</div>
</body>
</html>
```